Soy Candle Business needs a label design

We need a label design for a new company selling soy candles - Velvet Hearth Studio.

We are using apothecary jars in 3 sizes.
As per attached candles will be dressed with a beautiful black bow and all finished with a diamante in centre of bow.

We would like label done on lid of candle jars - 5cm circle (5cm from one side to the other), this way one label will fit each product size. Label will be done as a sticker.

We are thinking of the background colour to be black, however are open to recommendations. We want label to be classy, elegant and simple.

Inspiration for candle design came from attached invitation that features the bow, and beautiful vintage paper on top area.

Label should include the following 3 pieces of information:
Velvet Hearth Studio (company name)
Coconut Lime (this will change depending on fragrance)
Soy Candle

Velvet Hearth Studio does not have a company logo... what is done for the label will set tone for what is done across other elements of business moving forward.

Industry/Entity Type

Business

Requirements
Must have
• Velvet Hearth Studio
Fragrance Flavour
Soy Candle

```html
<!DOCTYPE html>
<html lang="en">
<head>
<meta charset="utf-8">
<title>Velvet Hearth Studio – Soy Candle Label</title>
<link rel="stylesheet" href="https://fonts.googleapis.com/css2?family=Alegreya:wght@400&family=Felipa&family=Pinyon+Script&display=swap">
<style>
  :root {
    --page: #ffffff;
    --label-black: #0b0b0b;
    --label-charcoal: #1e1e1e;
    --band-brown: #2e1a0b;
    --gold: #c8944a;
  }
  html, body {
    margin: 0;
    padding: 0;
    width: 1200px;
    height: 900px;
    overflow: hidden;
    background: var(--page);
  }
  .label-canvas {
    display: block;
    width: 1200px;
    height: 900px;
  }
  .studio-name {
    font-family: "Alegreya", "Cormorant Garamond", serif;
    font-size: 21px;
    letter-spacing: 1px;
    fill: var(--gold);
  }
  .fragrance-name {
    font-family: "Felipa", serif;
    font-size: 60px;
    letter-spacing: 2px;
    fill: var(--gold);
  }
  .product-type {
    font-family: "Pinyon Script", cursive;
    font-size: 42px;
    letter-spacing: 1px;
    fill: var(--gold);
  }
</style>
</head>
<body>
<svg class="label-canvas" viewBox="0 0 1200 900" xmlns="http://www.w3.org/2000/svg">
  <defs>
    <radialGradient id="label-ground" cx="50%" cy="50%" r="55%">
      <stop offset="0%" stop-color="var(--label-charcoal)"/>
      <stop offset="100%" stop-color="var(--label-black)"/>
    </radialGradient>
    <clipPath id="scallop-clip">
      <path id="scallop-path" d="M660.2 120.4
        A85 85 0 0 0 797.4 199.6
        A85 85 0 0 0 876.6 336.8
        A85 85 0 0 0 876.6 495.2
        A85 85 0 0 0 797.4 632.4
        A85 85 0 0 0 660.2 711.6
        A85 85 0 0 0 501.8 711.6
        A85 85 0 0 0 364.6 632.4
        A85 85 0 0 0 285.4 495.2
        A85 85 0 0 0 285.4 336.8
        A85 85 0 0 0 364.6 199.6
        A85 85 0 0 0 501.8 120.4
        A85 85 0 0 0 660.2 120.4 Z"/>
    </clipPath>
  </defs>

  <g class="scalloped-label" clip-path="url(#scallop-clip)">
    <rect class="label-ground" x="280" y="115" width="600" height="600"
          fill="url(#label-ground)" role="img"
          aria-label="Black background with faint dark-grey swirling damask flourishes"/>
    <g class="name-band">
      <rect x="280" y="384" width="600" height="79" fill="var(--band-brown)"/>
      <line x1="280" y1="384.5" x2="880" y2="384.5" stroke="var(--gold)" stroke-width="1"/>
      <line x1="280" y1="462.5" x2="880" y2="462.5" stroke="var(--gold)" stroke-width="1"/>
    </g>
  </g>

  <text class="studio-name" x="585" y="364" text-anchor="middle">Velvet Hearth Studio</text>
  <text class="fragrance-name" x="576" y="441" text-anchor="middle">Coconut Lime</text>
  <text class="product-type" x="586" y="528" text-anchor="middle">Soy Candle</text>
</svg>
</body>
</html>
```